Brivane LLC soda can design.

Welcome to Brivane luxury soda cans we offer five serious non sugar based flavors.

Soda, soda lime, soda green tea, soda tonic, soda ginger.

Plastic flag ship 750ml or 1l black label soda. Generic black label.
335 cans of same flag ship soda.

Thin tall 335 cans. Thin tall 250 cans. Normal 335 cans.

Files go to manufacturer for revision then back for final mastering.

Please center Image and scale all the same.

Pease be exact and consistent.

Transparent, white backgrounds for online selling and presentation.

Large gold font - Brivane tm
Small text - Established 2021 -
Small text with without copy.

Thank you.
Brivanellc@quenmail.com
Lumatrice@quenmail.com

Target Market(s)

Worldwide All ages generic soda

Industry/Entity Type

Soda water

Font styles to use
Serif
Decorative

Requirements
Must have
• Revisions after post manufacturer approval.
Nice to have
• 48706927 design generic soda
Should not have
• Non generic

```html
<!DOCTYPE html>
<html lang="en">
<head>
<meta charset="utf-8">
<title>Brivane Soda Can Labels</title>
<link href="https://fonts.googleapis.com/css2?family=Nunito+Sans:wght@300;400;600&display=swap" rel="stylesheet">
<style>
  :root {
    --bg: #e4e2de;
    --label-black: #1c1c1c;
    --label-edge: #141414;
    --texture-light: #2a2a2a;
    --gold: #c8a25a;
    --text-light: #e9e9e9;
    --band-soda: #d9b15f;
    --band-lime: #b8e21c;
    --band-green-tea: #12b04a;
    --band-tonic: #1187e0;
    --band-ginger: #ec6f22;
  }
  * { box-sizing: border-box; margin: 0; padding: 0; }
  html, body {
    width: 1200px;
    height: 768px;
    overflow: hidden;
    background: var(--bg);
    font-family: "Nunito Sans", Arial, sans-serif;
  }
  .range {
    position: absolute;
    top: 172px;
    left: 106px;
    display: flex;
    gap: 12px;
  }
  .can-label {
    position: relative;
    width: 188px;
    height: 468px;
    background: var(--label-black);
    border-radius: 3px;
    overflow: hidden;
    color: var(--text-light);
    text-align: center;
  }
  .label-texture {
    position: absolute;
    inset: 0;
    background: linear-gradient(90deg, var(--label-edge) 0%, var(--texture-light) 45%, var(--label-black) 70%, var(--label-edge) 100%);
  }
  .band {
    position: absolute;
    left: 0;
    right: 0;
    height: 4px;
    background: var(--accent);
  }
  .band--top { top: 18px; }
  .band--bottom { top: 450px; }
  .brand {
    position: absolute;
    top: 210px;
    width: 100%;
    font-size: 38px;
    font-weight: 600;
    letter-spacing: 1px;
    color: var(--gold);
    line-height: 1;
  }
  .established {
    position: absolute;
    top: 158px;
    width: 100%;
    font-size: 13px;
    font-weight: 400;
    letter-spacing: 0.6px;
  }
  .brand { top: 118px; }
  .flavour {
    position: absolute;
    top: 298px;
    width: 100%;
    font-size: 18px;
    font-weight: 300;
    letter-spacing: 0.4px;
    white-space: nowrap;
  }
  .volume {
    position: absolute;
    top: 418px;
    width: 100%;
    font-size: 13px;
    font-weight: 400;
    letter-spacing: 0.5px;
  }
  .volume .divider { margin: 0 3px; font-weight: 300; }
  .soda { --accent: var(--band-soda); }
  .lime { --accent: var(--band-lime); }
  .green-tea { --accent: var(--band-green-tea); }
  .tonic { --accent: var(--band-tonic); }
  .ginger { --accent: var(--band-ginger); }
</style>
</head>
<body>
  <main class="range">
    <section class="can-label soda">
      <div class="label-texture" role="img" aria-label="Fine dark wave line pattern across the label"></div>
      <span class="band band--top"></span>
      <h1 class="brand">Brivane</h1>
      <p class="established">Established 2021</p>
      <p class="flavour">SODA</p>
      <p class="volume">11.3 fl oz<span class="divider">|</span>335 ml</p>
      <span class="band band--bottom"></span>
    </section>
    <section class="can-label lime">
      <div class="label-texture" role="img" aria-label="Fine dark wave line pattern across the label"></div>
      <span class="band band--top"></span>
      <h2 class="brand">Brivane</h2>
      <p class="established">Established 2021</p>
      <p class="flavour">SODA LIME</p>
      <p class="volume">11.3 fl oz<span class="divider">|</span>335 ml</p>
      <span class="band band--bottom"></span>
    </section>
    <section class="can-label green-tea">
      <div class="label-texture" role="img" aria-label="Fine dark wave line pattern across the label"></div>
      <span class="band band--top"></span>
      <h2 class="brand">Brivane</h2>
      <p class="established">Established 2021</p>
      <p class="flavour">SODA GREEN TEA</p>
      <p class="volume">11.3 fl oz<span class="divider">|</span>335 ml</p>
      <span class="band band--bottom"></span>
    </section>
    <section class="can-label tonic">
      <div class="label-texture" role="img" aria-label="Fine dark wave line pattern across the label"></div>
      <span class="band band--top"></span>
      <h2 class="brand">Brivane</h2>
      <p class="established">Established 2021</p>
      <p class="flavour">SODA TONIC</p>
      <p class="volume">11.3 fl oz<span class="divider">|</span>335 ml</p>
      <span class="band band--bottom"></span>
    </section>
    <section class="can-label ginger">
      <div class="label-texture" role="img" aria-label="Fine dark wave line pattern across the label"></div>
      <span class="band band--top"></span>
      <h2 class="brand">Brivane</h2>
      <p class="established">Established 2021</p>
      <p class="flavour">SODA GINGER</p>
      <p class="volume">11.3 fl oz<span class="divider">|</span>335 ml</p>
      <span class="band band--bottom"></span>
    </section>
  </main>
</body>
</html>
```